M Zyvantics Buisness Cards

I need a technology focused clean business card for my employees. I have attached out logo to include in the mocks. We're a modern tech consulting firm that drives to interface humanity with technology in a truly cohesive fashion.

```html
<!DOCTYPE html>
<html lang="en">
<head>
<meta charset="utf-8">
<title>M Zyvantics Business Cards</title>
<link rel="stylesheet" href="https://fonts.googleapis.com/css2?family=Roboto:wght@400;700;900&display=swap">
<style>
  :root {
    --backdrop: #676767;
    --card-white: #ffffff;
    --brand-blue: #1c75bc;
    --brand-grey: #808285;
    --text-grey: #4d4d4f;
    --rule-grey: #e2e2e2;
  }
  * { margin: 0; padding: 0; box-sizing: border-box; }
  html, body {
    width: 1200px;
    height: 802px;
    overflow: hidden;
    background: var(--backdrop);
    font-family: "Roboto", Arial, sans-serif;
  }
  .canvas { position: relative; width: 1200px; height: 802px; }
  .card {
    position: absolute;
    top: 274px;
    width: 443px;
    height: 265px;
  }
  .card-front { left: 136px; background: var(--card-white); }
  .card-back { left: 624px; background: var(--brand-blue); }

  .brand {
    position: absolute;
    display: flex;
    align-items: center;
    gap: 8px;
    font-weight: 900;
    letter-spacing: 0.5px;
    white-space: nowrap;
  }
  .brand-dot { border-radius: 50%; flex: none; }
  .card-front .brand {
    left: 30px; top: 114px;
    font-size: 27px; color: var(--brand-grey);
  }
  .card-front .brand-dot { width: 16px; height: 16px; background: var(--brand-blue); }
  .card-back .brand {
    left: 0; right: 0; top: 108px; justify-content: center;
    font-size: 36px; color: var(--card-white);
  }
  .card-back .brand-dot { width: 22px; height: 22px; background: var(--card-white); }

  .divider {
    position: absolute;
    left: 232px; top: 58px;
    width: 1px; height: 140px;
    background: var(--rule-grey);
  }
  .contact-block { position: absolute; left: 254px; top: 76px; color: var(--text-grey); }
  .person-name { font-size: 14.5px; font-weight: 700; letter-spacing: 0.3px; line-height: 17px; }
  .person-name .first { color: var(--brand-blue); }
  .person-name .last { color: var(--brand-grey); }
  .person-role { font-size: 13px; line-height: 15px; }
  .contact-list { list-style: none; margin-top: 19px; }
  .contact-list li {
    display: flex; align-items: center; gap: 3px;
    font-size: 13px; line-height: 16px;
  }
  .contact-list svg { width: 10px; height: 10px; flex: none; fill: var(--brand-blue); }
</style>
</head>
<body>
<main class="canvas">
  <section class="card card-front">
    <div class="brand"><span class="brand-dot"></span>M Zyvantics</div>
    <div class="divider"></div>
    <div class="contact-block">
      <p class="person-name"><span class="first">DANIEL</span> <span class="last">MERCER</span></p>
      <p class="person-role">Managing Director</p>
      <ul class="contact-list">
        <li><svg viewBox="0 0 10 10"><path d="M1 4c0-2 2-3 4-3s4 1 4 3H7V3H3v1zM2 5h6l1 4H1z"/></svg>020-555 014 372</li>
        <li><svg viewBox="0 0 10 10"><path d="M2.5 0h5v10h-5zM3.5 1v7h3V1z"/></svg>020-555 014 372</li>
        <li><svg viewBox="0 0 10 10"><path d="M0 2h10v1L5 6 0 3zM0 4l5 3 5-3v4H0z"/></svg>info@zyvantics.com</li>
        <li><svg viewBox="0 0 10 10"><circle cx="5" cy="5" r="4.5"/></svg>www.zyvantics.com</li>
      </ul>
    </div>
  </section>
  <section class="card card-back">
    <div class="brand"><span class="brand-dot"></span>M Zyvantics</div>
  </section>
</main>
</body>
</html>
```